Clarinet Past Midnight: mini recital & soiree

I need a poster design for a recital I'm doing next Friday April 25. It's an "after party" from 10 - 1am where I'll be playing a 30 min program followed by a DJ and there'll be food wine etc. I want to see a very "sexy" kind of poster. Modern with a "south beach" kind of art deco feel but without the really cheesy connotation that south beach sometimes has (if that makes any sense). I've included the link for the Gatherlink event so you can get an idea of the feel I want.

Cheers!

https://www.gatherlink.example/events/519304762811095/

Target Market(s)

College Students at the Coral Ridge Institute

South Beach-ians

Industry/Entity Type

Events

Colors

Designer to choose colors to be used in the design.

Requirements
Must have
• Title of event..
Date..
Location..
Food / Beverage served..
DJ Torvik..

```html
<!DOCTYPE html>
<html lang="en">
<head>
<meta charset="utf-8">
<title>Clarinet Past Midnight — Mini Recital &amp; Soirée</title>
<link rel="stylesheet" href="https://fonts.googleapis.com/css2?family=Bebas+Neue&family=Josefin+Sans:wght@100;300&family=Quicksand:wght@400;500&display=swap">
<style>
  :root {
    --wall: #ecebe8;
    --paper: #ffffff;
    --night: #161415;
    --ink: #111111;
    --white: #ffffff;
    --coral: #f06c50;
    --ember: #e0573a;
    --violet: #7a2fb0;
  }
  * { margin: 0; padding: 0; box-sizing: border-box; }
  html, body { width: 1200px; height: 1152px; overflow: hidden; }
  body { background: var(--wall); position: relative; }

  .poster {
    position: absolute;
    left: 233px; top: 56px;
    width: 733px; height: 1040px;
    background: var(--night);
    overflow: hidden;
    box-shadow: 0 6px 20px rgba(0,0,0,0.18);
  }
  .poster__header {
    position: absolute; left: 0; top: 0;
    width: 100%; height: 190px;
    background: var(--paper);
  }
  .poster__atmosphere {
    position: absolute; left: 0; top: 190px;
    width: 100%; height: 758px;
    background:
      radial-gradient(ellipse 70% 28% at 40% 12%, rgba(122,47,176,0.28), transparent 70%),
      radial-gradient(ellipse 80% 30% at 50% 92%, rgba(224,87,58,0.32), transparent 72%);
  }
  .poster__title {
    position: absolute; left: 0; top: 0;
    width: 733px; height: 360px;
  }
  .poster__title text { font-family: "Josefin Sans", sans-serif; font-weight: 100; }
  .title__instrument { font-weight: 300 !important; }

  .lineup {
    position: absolute; left: 0; width: 100%;
    text-align: center;
  }
  .lineup__headline {
    top: 472px;
    font-family: "Bebas Neue", sans-serif;
    font-size: 82px; line-height: 1;
    color: var(--white);
    letter-spacing: 1px;
    padding-left: 14px;
  }
  .lineup__live {
    top: 545px;
    font-family: "Josefin Sans", sans-serif;
    font-weight: 300;
    font-size: 40px; line-height: 1;
    color: var(--coral);
    padding-left: 14px;
  }
  .lineup__dj {
    top: 622px;
    font-family: "Quicksand", sans-serif;
    font-weight: 500;
    font-size: 64px; line-height: 1;
    color: var(--white);
    letter-spacing: 2px;
  }
  .lineup__dj-note {
    top: 687px;
    font-family: "Quicksand", sans-serif;
    font-weight: 500;
    font-size: 20px; line-height: 1;
    color: var(--coral);
    letter-spacing: 1px;
  }

  .details {
    position: absolute; left: 0; top: 948px;
    width: 100%; height: 92px;
    background: var(--coral);
    color: var(--white);
    text-align: center;
    font-family: "Quicksand", sans-serif;
    padding-top: 12px;
  }
  .details__when { font-size: 25px; font-weight: 500; line-height: 1.1; letter-spacing: 0.5px; }
  .details__where,
  .details__catering { font-size: 13.5px; font-weight: 500; line-height: 1.35; letter-spacing: 0.5px; }
</style>
</head>
<body>
  <main class="poster">
    <div class="poster__header"></div>
    <div class="poster__atmosphere" role="img" aria-label="Scattered glowing particles, violet near the top and ember orange near the bottom"></div>

    <svg class="poster__title" viewBox="0 0 733 360" aria-label="Clarinet Past Midnight">
      <text class="title__instrument" x="0" y="0" font-size="22" fill="var(--ink)"
            transform="translate(206 190) rotate(-90)" textLength="146" lengthAdjust="spacingAndGlyphs">CLARINET</text>
      <text x="214" y="190" font-size="196" fill="var(--ink)"
            textLength="440" lengthAdjust="spacingAndGlyphs">PAST</text>
      <text x="150" y="340" font-size="196" fill="var(--white)"
            textLength="504" lengthAdjust="spacingAndGlyphs">MIDNIGHT</text>
    </svg>

    <h1 class="lineup lineup__headline">Mini Recital &amp; Soirée</h1>
    <p class="lineup lineup__live">LIVE</p>
    <h2 class="lineup lineup__dj">DJ TORVIK</h2>
    <p class="lineup lineup__dj-note">DJ SET FOR THE NIGHT</p>

    <footer class="details">
      <p class="details__when">FRIDAY, APRIL 25 AT 10:00PM - 1:00AM</p>
      <p class="details__where">HALVORSEN ALUMNI CENTER - CORAL RIDGE INSTITUTE</p>
      <p class="details__catering">FOOD / WINE / DRINK WILL BE SERVED!!</p>
    </footer>
  </main>
</body>
</html>
```